lumen crest business card project

Financial consulting in line with life insurance ,index annuity, college funding solutions. I educate clients on cash flow, debt management, how to create emergency fund, how to proper protection with the best insurance, how to accummulate asset and management, how to preserve asset/ estate planning. Collge funding solutions help familes seek the best funding solutions possible including award letter review and test prep on ACT, SAT, PSAT, SAT II
Target Market(s)
Individuals, family, business
Industry/Entity Type
Financial Planning
Contact Information for Business Card
Business name: Lumen Crest Financial Services
Odell Vink
Managing Director
License no. 7K24316
Address: 2815 Tarlow Ave. Fernhollow, OR 93482
Phone: 458-555-0148 Fax: 541-555-0193
Email: odell.vink@mailvora.com
Font styles to use
Other font styles liked:
- Bliss
Requirements
Must have
- Use feng shui as a guide to design the card make a flow curve lines only no angle or arrows.Size 3.5 inch by 2inch, metallic look is good, design a logo too . Keep it simple add image using feng shuis a guide. Also put a tagline that can make a very good impression. Use the back with something that the client we be able to use feng shui as guide.
Nice to have
- Use feng shui as guiding principle. Keep it simple
- Logo and tagline
Should not have
- Negative chi ,Angles, down ward design, too many things or too many images

```html
<!DOCTYPE html>
<html lang="en">
<head>
<meta charset="utf-8">
<title>Lumen Crest Financial Services – Business Card</title>
<link rel="stylesheet" href="https://fonts.googleapis.com/css2?family=Open+Sans:wght@400;600;700&family=Josefin+Sans:wght@300&display=swap">
<style>
  :root {
    --backdrop: #2b2b2b;
    --card: #111111;
    --card-edge: #1c1c1c;
    --accent: #e3202a;
    --ink: #f2f2f2;
    --ink-soft: #d6d6d6;
    --divider: #222222;
  }
  * { box-sizing: border-box; margin: 0; padding: 0; }
  html, body {
    width: 1200px; height: 900px; overflow: hidden;
    background: var(--backdrop);
  }
  .canvas {
    position: relative; width: 1200px; height: 900px;
    display: flex; align-items: center; justify-content: center; gap: 50px;
  }
  .card {
    position: relative;
    width: 500px; height: 286px;
    background: var(--card);
    border-radius: 20px;
    border: 1px solid var(--card-edge);
    box-shadow: 0 18px 40px rgba(0,0,0,.45);
    overflow: hidden;
  }
  /* Front */
  .card-front { display: flex; }
  .brand-panel {
    width: 200px; height: 100%;
    display: flex; align-items: center; justify-content: center; gap: 10px;
    border-right: 1px solid var(--divider);
  }
  .brand-dot {
    width: 14px; height: 14px; border-radius: 50%;
    background: var(--accent);
    flex: none;
  }
  .brand-name {
    font-family: "Open Sans", sans-serif;
    font-weight: 700; font-size: 22px;
    color: var(--accent);
    white-space: nowrap;
  }
  .details {
    flex: 1; padding: 48px 0 0 34px;
    font-family: "Open Sans", sans-serif;
    color: var(--ink);
  }
  .person-name {
    font-weight: 700; font-size: 19px; color: var(--accent); line-height: 1.1;
  }
  .person-title { font-size: 13px; color: var(--ink-soft); margin-top: 2px; }
  .address { font-size: 14px; line-height: 1.45; margin-top: 20px; }
  .contacts { list-style: none; margin-top: 18px; font-size: 14px; }
  .contacts li { display: flex; align-items: center; gap: 12px; line-height: 1.55; white-space: nowrap; }
  .contacts svg { width: 12px; height: 12px; fill: var(--accent); flex: none; }
  /* Back */
  .card-back {
    display: flex; align-items: center; justify-content: center;
  }
  .back-wordmark {
    display: flex; flex-direction: column; align-items: flex-end;
    font-family: "Josefin Sans", sans-serif;
    font-weight: 300;
    color: var(--ink);
  }
  .back-name { font-size: 44px; line-height: 1; letter-spacing: .5px; }
  .back-sub {
    font-size: 12px; letter-spacing: 1.2px; text-transform: uppercase;
    margin-top: 2px; margin-right: 34px;
  }
</style>
</head>
<body>
<main class="canvas">
  <section class="card card-front" aria-label="Business card front">
    <div class="brand-panel">
      <span class="brand-dot"></span>
      <span class="brand-name">Lumen Crest</span>
    </div>
    <div class="details">
      <p class="person-name">Odell Vink</p>
      <p class="person-title">Managing Director</p>
      <p class="address">2815 Tarlow Ave.<br>Fernhollow, OR 93482</p>
      <ul class="contacts">
        <li>
          <svg viewBox="0 0 24 24" aria-hidden="true"><path d="M6.6 10.8a15.1 15.1 0 0 0 6.6 6.6l2.2-2.2a1 1 0 0 1 1-.25 11.4 11.4 0 0 0 3.6.57 1 1 0 0 1 1 1V20a1 1 0 0 1-1 1A17 17 0 0 1 3 4a1 1 0 0 1 1-1h3.5a1 1 0 0 1 1 1c0 1.25.2 2.45.57 3.57a1 1 0 0 1-.25 1z"/></svg>
          458-555-0148
        </li>
        <li>
          <svg viewBox="0 0 24 24" aria-hidden="true"><path d="M6 2h9l3 3v5h1a2 2 0 0 1 2 2v8a2 2 0 0 1-2 2H5a2 2 0 0 1-2-2v-8a2 2 0 0 1 2-2h1zm2 2v6h8V6h-2V4zm-1 10v2h2v-2zm4 0v2h2v-2zm4 0v2h2v-2z"/></svg>
          541-555-0193
        </li>
        <li>
          <svg viewBox="0 0 24 24" aria-hidden="true"><path d="M2 5h20v14H2zm2 2v.5l8 5 8-5V7zm0 2.8V17h16V9.8l-8 5z"/></svg>
          odell.vink@mailvora.com
        </li>
      </ul>
    </div>
  </section>

  <section class="card card-back" aria-label="Business card back">
    <p class="back-wordmark">
      <span class="back-name">Lumen Crest</span>
      <span class="back-sub">Financial Services</span>
    </p>
  </section>
</main>
</body>
</html>
```